Eye catching Stationary Design

Healthcare consultant firm looking for stationary design ( letterhead, envelope and business cards) That’s professional, classy and eye catching . The design should incorporate the logo and the colors of the logo in its design. You can see the logo on our website at www harbor key advisors. com.

```html
<!DOCTYPE html>
<html lang="en">
<head>
<meta charset="utf-8">
<title>Harbor Key Advisors — Letterhead</title>
<link rel="stylesheet" href="https://fonts.googleapis.com/css2?family=Open+Sans:wght@400;600&family=Arimo:wght@700&display=swap">
<style>
  :root {
    --brand-navy: #0b57a6;
    --brand-sky: #2ea3dc;
    --paper: #ffffff;
    --backdrop: #e4e5e7;
    --ink: #3a3a3a;
    --ink-strong: #2b2b2b;
    --signature-tone: #d9d9d9;
  }
  * { margin: 0; padding: 0; box-sizing: border-box; }
  html, body {
    width: 1200px; height: 945px; overflow: hidden;
    background: var(--backdrop);
  }
  .letterhead {
    position: absolute; left: 289px; top: 32px;
    width: 622px; height: 880px;
    background: var(--paper);
    box-shadow: 0 2px 10px rgba(0,0,0,0.12);
    overflow: hidden;
    font-family: "Open Sans", Arial, sans-serif;
    color: var(--ink);
  }
  .header-art { position: absolute; left: 0; top: 0; }
  .contact {
    position: absolute; left: 456px; top: 10px;
    color: var(--paper);
    font-size: 7.5px; line-height: 10.5px;
    list-style: none;
  }
  .contact li { display: flex; align-items: center; gap: 5px; white-space: nowrap; }
  .contact svg { flex: none; }
  .brand {
    position: absolute; left: 40px; top: 66px;
    display: flex; align-items: center; gap: 10px;
  }
  .brand-mark { width: 30px; height: 30px; background: var(--brand-sky); }
  .brand-name {
    font-size: 11px; line-height: 12px; font-weight: 400;
    font-variant: small-caps; letter-spacing: 0.6px;
    color: var(--brand-navy);
  }
  .letter-body {
    position: absolute; left: 58px; top: 208px; width: 480px;
  }
  .salutation {
    font-family: "Arimo", Arial, sans-serif; font-weight: 700;
    font-size: 13px; color: var(--ink-strong); margin-bottom: 8px;
  }
  .letter-body p {
    font-size: 11.5px; line-height: 15.5px; margin-bottom: 16px;
    text-align: justify;
  }
  .signature {
    position: absolute; left: 60px; top: 585px;
    width: 150px; height: 44px;
    background: linear-gradient(90deg, var(--signature-tone), #f0f0f0);
    border-radius: 4px;
  }
  .footer-art { position: absolute; left: 0; bottom: 0; }
</style>
</head>
<body>
<main class="letterhead">
  <svg class="header-art" width="622" height="120" viewBox="0 0 622 120" aria-hidden="true">
    <path d="M330,0 H622 V96 H452 C420,96 412,70 392,58 C372,46 352,40 330,40 Z" fill="var(--brand-navy)"/>
    <path d="M0,40 H330" stroke="var(--brand-navy)" stroke-width="6" fill="none"/>
    <path d="M0,49 H320 C350,49 372,54 392,66 C412,80 420,104 452,104 H462" stroke="var(--brand-sky)" stroke-width="3" fill="none"/>
  </svg>

  <ul class="contact">
    <li>418 Meridian Street Portland,</li>
    <li>Oregon Suite B12</li>
    <li>
      <svg width="8" height="8" viewBox="0 0 8 8"><path d="M1,1 L3,1 L3.5,3 L2.5,3.6 C3,4.8 3.6,5.4 4.6,5.8 L5.2,4.8 L7,5.4 L7,7 C3.5,7 1,4.5 1,1 Z" fill="#fff"/></svg>
      (503) 555-0142
    </li>
    <li>
      <svg width="8" height="8" viewBox="0 0 8 8"><rect x="0.5" y="1.5" width="7" height="5" fill="none" stroke="#fff"/><path d="M0.5,1.5 L4,4.5 L7.5,1.5" fill="none" stroke="#fff"/></svg>
      info@harborkeyadvisors.com
    </li>
    <li>
      <svg width="8" height="8" viewBox="0 0 8 8"><circle cx="4" cy="4" r="3.3" fill="none" stroke="#fff"/><path d="M0.7,4 H7.3 M4,0.7 V7.3" stroke="#fff" stroke-width="0.7"/></svg>
      www.harborkeyadvisors.com
    </li>
  </ul>

  <div class="brand">
    <span class="brand-mark"></span>
    <span class="brand-name">Harbor Key<br>Advisors<br>LLC</span>
  </div>

  <section class="letter-body">
    <p class="salutation">Dear Mr. John,</p>
    <p>Lorem Ipsum is simply dummy text of the printing and typesetting industry. Lorem Ipsum has been the industry's standard dummy text ever since the 1500s, when an unknown printer took a galley of type and scrambled it to make a type specimen book. It has survived not only five centuries, but also the leap into electronic typesetting, remaining essentially unchanged.</p>
    <p>The standard chunk of Lorem Ipsum used since the 1500s is reproduced below for those interested. Sections 1.10.32 and 1.10.33 from "de Ordine Rerum Novarum" by Varro Lentulus are also reproduced in their exact original form, accompanied by English versions from the 1914 translation by M. Ashdown</p>
    <p>Lorem Ipsum is simply dummy text of the printing and typesetting industry. Lorem Ipsum has been the industry's standard dummy text ever since the 1500s, when an unknown printer took a galley of type and scrambled it to make a type specimen book. It has survived not only five centuries, but also the leap into electronic typesetting, remaining essentially unchanged. It was popularised in the</p>
    <p>The standard chunk of Lorem Ipsum used since the 1500s is reproduced below for those interested. Sections 1.10.32 and 1.10.33 from "de Ordine Rerum Novarum" by Varro Lentulus are also reproduced in their exact original form, accompanied by English versions from the 1914 translation by M. Ashdown</p>
  </section>

  <div class="signature" role="img" aria-label="Handwritten signature of the sender"></div>

  <svg class="footer-art" width="622" height="90" viewBox="0 0 622 90" aria-hidden="true">
    <rect x="0" y="30" width="622" height="60" fill="var(--brand-navy)"/>
    <rect x="48" y="0" width="526" height="50" rx="10" fill="var(--paper)"/>
    <path d="M56,44 H566" stroke="var(--brand-sky)" stroke-width="3" stroke-linecap="round"/>
  </svg>
</main>
</body>
</html>
```